Business Card Design Project

Hello Designers, hope you are all aiming enjoy the weekend
I have the Business Logo (uploaded), you can alter the color which ever way you think would work,
Im looking for a simple yet striking feel, something which will stay memorable (I have uploaded 3 examples for you to flick through)
Information on the card, will just be the bare minimum,
Double Sided
Info being
i.e.
Name
Number
Website
ABN
Tobin Wexmoor
+468213579 (singapore)
+315792846 (Australia)
+729384615 (America)
www.lomevu-linkup.example
ABN 86420913
Enjoy,
Tobin
Industry/Entity Type
Business
Look and feel
Each slider illustrates characteristics of the customer's brand and the style your logo design should communicate.

```html
<!DOCTYPE html>
<html lang="en">
<head>
<meta charset="utf-8">
<title>Lomevu Linkup – Business Card</title>
<link rel="stylesheet" href="https://fonts.googleapis.com/css2?family=Arimo:wght@400;700&display=swap">
<style>
  :root {
    --backdrop: #e6eef0;
    --card: #ffffff;
    --band-pink: #e8308f;
    --text-pink: #e0308a;
    --brand-red: #d2154a;
    --brand-red-deep: #b80d3c;
    --shadow: rgba(60, 80, 90, 0.22);
  }
  * { box-sizing: border-box; margin: 0; padding: 0; }
  html, body {
    width: 1200px;
    height: 900px;
    overflow: hidden;
    background: var(--backdrop);
    font-family: "Arimo", Arial, sans-serif;
  }
  .canvas {
    position: relative;
    width: 1200px;
    height: 900px;
  }
  .card {
    position: absolute;
    width: 652px;
    height: 415px;
    background: var(--card);
    border-radius: 14px;
    overflow: hidden;
    box-shadow: 0 3px 8px var(--shadow);
  }
  .card--front { left: 33px; top: 18px; }
  .card--back { left: 518px; top: 463px; }
  .card__band {
    position: absolute;
    left: 0;
    right: 0;
    bottom: 0;
    height: 43px;
    background: var(--band-pink);
  }
  .wordmark {
    position: absolute;
    left: 0;
    right: 0;
    top: 168px;
    display: flex;
    align-items: center;
    justify-content: center;
    gap: 20px;
  }
  .wordmark__square {
    width: 70px;
    height: 70px;
    border-radius: 10px;
    background: var(--brand-red);
  }
  .wordmark__name {
    font-size: 52px;
    font-weight: 400;
    color: var(--brand-red);
    letter-spacing: 0.5px;
  }
  .brand-square {
    position: absolute;
    left: 107px;
    top: 137px;
    width: 142px;
    height: 142px;
    border-radius: 16px;
    background: linear-gradient(160deg, var(--brand-red) 0%, var(--brand-red-deep) 100%);
  }
  .divider {
    position: absolute;
    left: 325px;
    top: 112px;
    width: 4px;
    height: 172px;
    background: linear-gradient(to bottom, rgba(232,48,143,0) 0%, var(--band-pink) 30%, var(--band-pink) 70%, rgba(232,48,143,0) 100%);
  }
  .contact {
    position: absolute;
    left: 361px;
    top: 74px;
    color: var(--text-pink);
    font-weight: 700;
  }
  .contact__name {
    font-size: 34px;
    line-height: 44px;
    margin-bottom: 14px;
  }
  .contact__list {
    list-style: none;
    padding-left: 10px;
    font-size: 18.5px;
    line-height: 25px;
  }
</style>
</head>
<body>
  <main class="canvas">
    <section class="card card--front" aria-label="Card front">
      <div class="wordmark">
        <span class="wordmark__square" aria-hidden="true"></span>
        <span class="wordmark__name">Lomevu Linkup</span>
      </div>
      <div class="card__band"></div>
    </section>

    <section class="card card--back" aria-label="Card back">
      <div class="brand-square" aria-hidden="true"></div>
      <div class="divider" aria-hidden="true"></div>
      <div class="contact">
        <h1 class="contact__name">Tobin Wexmoor</h1>
        <ul class="contact__list">
          <li>+468213579 (singapore)</li>
          <li>+315792846 (Australia)</li>
          <li>+729384615 (America)</li>
          <li>www.lomevu-linkup.example</li>
          <li>ABN 86420913</li>
        </ul>
      </div>
      <div class="card__band"></div>
    </section>
  </main>
</body>
</html>
```